Looking for a contemporary business card design with our logo

would like to consider a embossing look although I'm not married to the idea. We are a custom jeweler that needs a look that represents old world craftsmanship with a modern twist that's why we went with a more modern shield type of logo that can be stamped inside our rings.
It could be two sided or one we are more after a look the pops and is trendy and creative. (WE ARE NOT LOOKING FOR A COOKIE CUTTER LAYOUT)
We have attached the image and will be using the logo with harwick studio wording in the format that it's in unless you see a better way of doing it.
If the logo needs a twist we are O.K. with suggestions as well.
This card should scream "Quality" from a high end studio.
Harwick Studio
4186 Maplecrest Rd. Unit B-2
Alderton, WY 80317
www.harwickstudio-example.com
lu@harwickstudio-example.com
Should speak quality craftsmanship

```html
<!DOCTYPE html>
<html lang="en">
<head>
<meta charset="utf-8">
<title>Harwick Studio — Business Card</title>
<link href="https://fonts.googleapis.com/css2?family=Open+Sans:wght@400;600&display=swap" rel="stylesheet">
<style>
  :root {
    --backdrop: #2a2624;
    --card-black: #1c1c1d;
    --card-black-deep: #121213;
    --silver-light: #e4e4e4;
    --silver-mid: #b9b9b9;
    --silver-dark: #8d8d8d;
    --text-light: #dcdcdc;
    --text-muted: #bdbdbd;
    --emboss: #2b2b2c;
  }
  * { box-sizing: border-box; margin: 0; padding: 0; }
  html, body {
    width: 1200px; height: 680px; overflow: hidden;
    background: var(--backdrop);
    font-family: "Open Sans", Arial, sans-serif;
  }
  .canvas {
    position: relative; width: 1200px; height: 680px;
    background: radial-gradient(ellipse at 65% 40%, #3a3532 0%, var(--backdrop) 70%);
  }
  .card {
    position: absolute; top: 185px; width: 540px; height: 310px;
    border-radius: 6px; overflow: hidden;
    background: linear-gradient(160deg, var(--card-black) 0%, var(--card-black-deep) 100%);
    box-shadow: 0 18px 40px rgba(0,0,0,.55);
  }
  .card--back { left: 40px; }
  .card--front { left: 620px; }

  /* back side */
  .back-wordmark {
    position: absolute; top: 90px; left: 0; right: 0; text-align: center;
  }
  .back-wordmark .wordmark-name {
    color: var(--emboss); font-size: 34px; font-weight: 600;
    letter-spacing: 3px; text-transform: uppercase;
  }
  .silver-band-horizontal {
    position: absolute; left: 0; right: 0; top: 224px; height: 42px;
    background: linear-gradient(90deg, var(--silver-dark), var(--silver-light) 45%, var(--silver-mid));
    display: flex; align-items: center; padding-left: 130px;
  }
  .band-url {
    color: #4a4a4a; font-size: 14px; letter-spacing: 2px;
  }

  /* front side */
  .silver-band-vertical {
    position: absolute; top: 0; bottom: 0; left: 62px; width: 44px;
    background: linear-gradient(180deg, var(--silver-mid), var(--silver-light) 40%, var(--silver-dark));
  }
  .band-square {
    position: absolute; top: 26px; left: 8px; width: 28px; height: 28px;
    background: var(--card-black); border: 2px solid var(--silver-light);
  }
  .contact {
    position: absolute; left: 116px; top: 118px; width: 240px; color: var(--text-light);
  }
  .contact-name { font-size: 19px; margin-bottom: 6px; }
  .contact-line {
    font-size: 13px; line-height: 19px; color: var(--text-muted);
    display: flex; align-items: center; gap: 6px; white-space: nowrap;
  }
  .contact-line svg { flex: none; }
  .front-wordmark {
    position: absolute; right: 22px; top: 120px; width: 150px; text-align: center;
  }
  .front-wordmark .wordmark-name {
    color: var(--silver-mid); font-size: 25px; font-weight: 600;
    letter-spacing: 2px; text-transform: uppercase; line-height: 1.25;
  }
</style>
</head>
<body>
<main class="canvas">
  <section class="card card--back" aria-label="Card back">
    <div class="back-wordmark"><span class="wordmark-name">Harwick Studio</span></div>
    <div class="silver-band-horizontal"><span class="band-url">www.harwickstudio-example.com</span></div>
  </section>

  <section class="card card--front" aria-label="Card front">
    <div class="silver-band-vertical"><span class="band-square"></span></div>
    <div class="contact">
      <p class="contact-name">Harwick Studio</p>
      <p class="contact-line">4186 Maplecrest Rd. Unit B-2</p>
      <p class="contact-line">Alderton, WY 80317</p>
      <p class="contact-line">
        <svg width="11" height="8" viewBox="0 0 11 8"><rect x=".5" y=".5" width="10" height="7" fill="none" stroke="currentColor"/><path d="M.5 .5 5.5 4.5 10.5 .5" fill="none" stroke="currentColor"/></svg>
        lu@harwickstudio-example.com
      </p>
      <p class="contact-line">
        <svg width="11" height="9" viewBox="0 0 11 9"><rect x=".5" y=".5" width="10" height="6" fill="none" stroke="currentColor"/><path d="M3 8.5h5" stroke="currentColor"/></svg>
        www.harwickstudio-example.com
      </p>
    </div>
    <div class="front-wordmark"><span class="wordmark-name">Harwick Studio</span></div>
  </section>
</main>
</body>
</html>
```